I teach courses in Quick Phrases for Rescue Crews, paramedics, firefighters, nurses and all other Emergency related occupations. I need to let them know that this course is available and post this card on the bulletin boards of fire stations and other related offices. It has to call their attention.

Industry/Entity Type

Call

Colors
ec2027

Requirements
Must have
• I would like a picture of a paramedic and a nurse. It can also have a firefighter as a second choice. Red is a good color to call attention. I am including a picture of me and a short bio to go on the reverse but this is not a must. I do not want my picture in the front.
I am thinking of an over sized postcard
Nice to have
• The title can be "Quick Phrases for Rescue Crews" in full or "Quick Phrases for RC's " depending on the fact that the whole name may be too long to make it stand out enough
Should not have
• I do not know if my picture has come out in the right frame I see the cut is not right in the uploead. You might need to frame it right.

```html
<!DOCTYPE html>
<html lang="en">
<head>
<meta charset="utf-8">
<title>Quick Phrases for Rescue Crews – Postcard, front and back</title>
<link href="https://fonts.googleapis.com/css2?family=Didact+Gothic&family=Poppins:wght@400;600;700&display=swap" rel="stylesheet">
<style>
  :root{
    --red:#ec2027;
    --blue:#1a6fc0;
    --ink:#2b2b2b;
    --panel-light:#f4f4f5;
    --panel-mid:#d9dadc;
    --back-bg:#f7f7f8;
    --page:#ecebe8;
    --white:#ffffff;
  }
  *{box-sizing:border-box;margin:0;padding:0}
  html,body{width:1200px;height:1000px;overflow:hidden;background:var(--page)}
  body{display:flex;flex-direction:column;align-items:center;justify-content:center;gap:16px;font-family:"Didact Gothic",sans-serif;color:var(--ink)}
  .postcard{width:760px;height:476px;box-shadow:0 4px 14px rgba(0,0,0,.18);flex:none}

  /* Front */
  .postcard--front{display:flex;flex-direction:column;background:linear-gradient(180deg,var(--panel-light) 0%,var(--panel-mid) 100%)}
  .header{background:var(--red);height:100px;color:var(--white);text-align:center;display:flex;flex-direction:column;justify-content:center;border-bottom:6px solid var(--blue);flex:none}
  .header__kicker{font-family:"Poppins",sans-serif;font-weight:400;font-size:24px;line-height:1.05}
  .header__title{font-family:"Poppins",sans-serif;font-weight:700;font-size:42px;line-height:1.1;letter-spacing:-.3px}
  .body{flex:1;padding:12px 44px 0;display:flex;flex-direction:column}
  .intro{text-align:center;font-size:17px;line-height:1.25}
  .intro strong{color:var(--red);font-family:"Poppins",sans-serif;font-weight:600}
  .benefits{list-style:none;margin-top:8px}
  .benefits li{display:flex;align-items:center;gap:12px;font-size:13.5px;line-height:1.3}
  .bullet{width:12px;height:12px;flex:none}
  .photos{display:flex;gap:8px;margin-top:auto}
  .photo{flex:1;height:82px;border:2px solid #9a9a9a}
  .photo--nurse{background:linear-gradient(135deg,#e7ecf0,#3c6fa8)}
  .photo--fire{background:linear-gradient(135deg,#f6b13a,#c2410c 60%,#5a1a08)}
  .photo--paramedic{background:linear-gradient(135deg,#2f4f7a,#8aa0bd 60%,#d9c7b5)}
  .availability{background:var(--red);color:var(--white);text-align:center;padding:6px 0 5px;font-size:15px;line-height:1.25;flex:none}
  .availability strong{font-family:"Poppins",sans-serif;font-weight:700}
  .contact{background:var(--blue);color:var(--white);text-align:center;padding:7px 0 9px;font-size:12.5px;flex:none}
  .contact strong{font-family:"Poppins",sans-serif;font-weight:600}

  /* Back */
  .postcard--back{background:var(--back-bg);position:relative;padding:28px 40px}
  .portrait{width:190px;height:230px;background:linear-gradient(160deg,#8a7766,#3e342d);border:2px solid #c9c9c9}
  .bio{position:absolute;left:40px;right:40px;bottom:34px;text-align:center;font-size:14.5px;line-height:1.45}
  .bio__text{margin-bottom:14px}
  .bio__contact{font-size:14.5px}
  .bio__contact .network{color:var(--blue);font-family:"Poppins",sans-serif;font-weight:600}
  .bio__contact strong{font-family:"Poppins",sans-serif;font-weight:600}
</style>
</head>
<body>
  <article class="postcard postcard--front">
    <header class="header">
      <div class="header__kicker">Quick Phrases for</div>
      <h1 class="header__title">Rescue Crews</h1>
    </header>
    <section class="body">
      <p class="intro">Course designed specifically for <strong>paramedics, firefighters, nurses</strong><br>and all other <strong>emergency related occupations.</strong></p>
      <ul class="benefits">
        <li><svg class="bullet" viewBox="0 0 18 18"><circle cx="9" cy="9" r="8" fill="none" stroke="#ec2027" stroke-width="2"/><circle cx="9" cy="9" r="4.5" fill="#ec2027"/></svg>Learn exactly the language you need for each emergency situation</li>
        <li><svg class="bullet" viewBox="0 0 18 18"><circle cx="9" cy="9" r="8" fill="none" stroke="#ec2027" stroke-width="2"/><circle cx="9" cy="9" r="4.5" fill="#ec2027"/></svg>Bring down the language barrier with your Spanish-speaking patients</li>
        <li><svg class="bullet" viewBox="0 0 18 18"><circle cx="9" cy="9" r="8" fill="none" stroke="#ec2027" stroke-width="2"/><circle cx="9" cy="9" r="4.5" fill="#ec2027"/></svg>Earn credits for your job or resume</li>
        <li><svg class="bullet" viewBox="0 0 18 18"><circle cx="9" cy="9" r="8" fill="none" stroke="#ec2027" stroke-width="2"/><circle cx="9" cy="9" r="4.5" fill="#ec2027"/></svg>Meet new people while you practice</li>
        <li><svg class="bullet" viewBox="0 0 18 18"><circle cx="9" cy="9" r="8" fill="none" stroke="#ec2027" stroke-width="2"/><circle cx="9" cy="9" r="4.5" fill="#ec2027"/></svg>Build a solid base for speaking Spanish in any situation sounding like a native</li>
        <li><svg class="bullet" viewBox="0 0 18 18"><circle cx="9" cy="9" r="8" fill="none" stroke="#ec2027" stroke-width="2"/><circle cx="9" cy="9" r="4.5" fill="#ec2027"/></svg>Learn easily with " whole brain learning tools"</li>
        <li><svg class="bullet" viewBox="0 0 18 18"><circle cx="9" cy="9" r="8" fill="none" stroke="#ec2027" stroke-width="2"/><circle cx="9" cy="9" r="4.5" fill="#ec2027"/></svg>Learn more about yourself and how you learn best</li>
        <li><svg class="bullet" viewBox="0 0 18 18"><circle cx="9" cy="9" r="8" fill="none" stroke="#ec2027" stroke-width="2"/><circle cx="9" cy="9" r="4.5" fill="#ec2027"/></svg>Have great fun and de-stress</li>
      </ul>
      <div class="photos">
        <div class="photo photo--nurse" role="img" aria-label="Photo of a nurse in blue scrubs holding a clipboard"></div>
        <div class="photo photo--fire" role="img" aria-label="Photo of firefighters spraying water at flames"></div>
        <div class="photo photo--paramedic" role="img" aria-label="Photo of paramedics performing CPR on a patient"></div>
      </div>
    </section>
    <p class="availability">Small groups and one-on-one coaching/tutoring sessions available in<br><strong>Santa Monica, California.</strong></p>
    <p class="contact">For more information find us on <strong>Linkside as Marisol Averly</strong> or <strong>Call: 310 5550148</strong></p>
  </article>

  <article class="postcard postcard--back">
    <div class="portrait" role="img" aria-label="Portrait photo of the course instructor"></div>
    <div class="bio">
      <p class="bio__text">Marisol Averly was raised in Argentina. Drawing from a superb blend of skills,<br>she is able to teach unique courses in Spanish for professionals. Her native<br>Spanish, "castellano" from Argentina, her many years of experience<br>in linguistics and her studies in Life Coaching, Transformational Coaching and<br>various other fields assures you a one of a kind language learning experience.</p>
      <p class="bio__contact">Find more on <span class="network">Linkside</span> as <strong>Marisol Averly</strong> or <strong>Call (310) 5550148</strong></p>
    </div>
  </article>
</body>
</html>
```